Branded PowerPoint Template Design

Would like a general PowerPoint template customized with my company branding to use in presentations for customers. The company is a talent management consulting and recruiting company called Brenwick & Associates. I would like a design that incorporates the logo colors with a clean and simple look.
Target Market(s)
Slides are typically viewed by HR and Corporate executives either briefing our capabilities or delivering solution results.
Industry/Entity Type
It Company
Requirements
Must have
- Simple clean design that will not draw attention away from the actual presentation. Design should go well with the logo branding and colors.
Should not have
- Should not have any pictures of people

```html
<!DOCTYPE html>
<html lang="en">
<head>
<meta charset="utf-8">
<title>Brenwick &amp; Associates — Presentation Template</title>
<link rel="stylesheet" href="https://fonts.googleapis.com/css2?family=Roboto+Condensed:wght@400;700&family=Open+Sans:wght@400;600;700&display=swap">
<style>
  :root{
    --navy:#1f0f6b;
    --navy-2:#2a1580;
    --violet:#3b1aa0;
    --ink:#333;
    --muted:#555;
    --rule:#a9a9ab;
    --panel:#f1f1f3;
    --cyan:#22b7d6;
    --slate:#5d5f66;
    --teal-gray:#8eaaa7;
  }
  *{box-sizing:border-box;margin:0;padding:0}
  html,body{width:1200px;height:1200px;overflow:hidden;background:#fff}
  body{position:relative;font-family:"Open Sans",Arial,sans-serif;color:var(--ink)}
  .slide{position:absolute;width:386px;height:291px;background:#fff;overflow:hidden;box-shadow:0 0 0 1px #e4e4e8}
  .slide::after{content:"";position:absolute;left:0;right:0;bottom:0;height:12px;background:var(--rule)}
  .c1{left:12px}.c2{left:407px}.c3{left:801px}
  .r1{top:10px}.r2{top:307px}.r3{top:605px}.r4{top:902px}

  .header{position:absolute;left:0;top:0;width:100%;height:39px;background:var(--navy);display:flex;align-items:center;justify-content:space-between;padding:0 9px}
  .header h2{font-family:"Roboto Condensed",Arial,sans-serif;font-weight:700;font-size:19px;color:#fff;letter-spacing:.2px}
  .brand{font-family:"Roboto Condensed",Arial,sans-serif;font-weight:700;color:#fff;font-size:11px;line-height:11px;text-align:right}
  .body{position:absolute;left:0;top:39px;right:0;bottom:12px}

  .cover-band{position:absolute;left:0;top:0;width:100%;height:164px;background:var(--navy)}
  .cover-title{position:absolute;font-family:"Roboto Condensed",Arial,sans-serif;font-weight:700;font-size:20px;color:#fff}
  .cover-sub{position:absolute;font-family:"Roboto Condensed",Arial,sans-serif;font-size:8.5px;line-height:11px;color:#fff}
  .cover-logo{position:absolute;left:0;right:0;top:190px;text-align:center}
  .cover-logo .mark{display:block;width:22px;height:22px;border-radius:50%;background:var(--navy);margin:0 auto 6px}
  .cover-logo .name{font-family:"Roboto Condensed",Arial,sans-serif;font-weight:700;font-size:22px;color:var(--navy)}

  .small{font-size:5.6px;line-height:9px;color:var(--muted)}
  .h-violet{font-family:"Open Sans",Arial,sans-serif;font-weight:600;color:var(--violet)}
  .abs{position:absolute}

  .bullets li{list-style:none;display:flex;align-items:center;font-size:8.4px;color:#333;height:25px}
  .bullets li::before{content:"";width:11px;height:11px;border-radius:50%;background:var(--navy);margin-right:8px;flex:none}

  .card{position:absolute;top:131px;width:106px;height:130px;border:1px solid #9aa0c9;background:#fff}
  .card h4{height:20px;color:#fff;font-family:"Roboto Condensed",Arial,sans-serif;font-size:7.5px;text-align:center;line-height:20px}
  .card p{padding:7px 11px;font-size:5.4px;line-height:9.7px;color:#555}
  .year{position:absolute;top:91px;width:34px;height:34px;border-radius:50%;border:3px solid #cfcfd8;color:#fff;font-family:"Roboto Condensed",Arial,sans-serif;font-weight:700;font-size:10px;display:flex;align-items:center;justify-content:center}

  .ph{position:absolute;background:var(--panel)}

  .chev{position:absolute;left:17px;width:48px;height:46px}
  .chev span{position:absolute;left:0;right:0;top:14px;text-align:center;color:#fff;font-family:"Roboto Condensed",Arial,sans-serif;font-weight:700;font-size:8px}
  .tbox{position:absolute;left:65px;width:303px;height:32px;border:1px solid #7a7fc4;border-left:none;border-radius:0 3px 3px 0;padding:3px 6px;font-size:7.2px;line-height:12.5px;color:#4a3cae}

  .thanks-box{position:absolute;left:205px;top:93px;width:181px;height:120px;background:#fff;padding:14px 18px;font-size:9.4px;line-height:12.5px;color:#444}
</style>
</head>
<body>

<section class="slide c1 r1">
  <div class="cover-band"></div>
  <h1 class="cover-title" style="left:0;right:0;top:63px;text-align:center">Project Title Here</h1>
  <p class="cover-sub" style="left:0;right:0;top:92px;text-align:center">Subtext here Here Subtext here Here Subtext<br>here Here Subtext here Here</p>
  <div class="cover-logo"><span class="mark"></span><span class="name">Brenwick &amp; Associates</span></div>
</section>

<section class="slide c2 r1">
  <div class="cover-band"></div>
  <h1 class="cover-title" style="right:27px;top:72px;text-align:right">Project Title Here</h1>
  <p class="cover-sub" style="right:27px;top:103px;text-align:right">Subtext here Here Subtext here Here Subtext<br>here Here Subtext here Here</p>
  <div class="cover-logo"><span class="mark"></span><span class="name">Brenwick &amp; Associates</span></div>
</section>

<section class="slide c3 r1">
  <header class="header"><h2>Project Title Here</h2><div class="brand">Brenwick &amp;<br>Associates</div></header>
  <div class="body">
    <svg width="386" height="240" viewBox="0 0 386 240" aria-hidden="true">
      <g transform="translate(192 101)" fill="none" stroke-width="13">
        <circle r="62" stroke="#2a1580" stroke-dasharray="50 339.6" transform="rotate(-118)"/>
        <circle r="62" stroke="#2a1580" stroke-dasharray="50 339.6" transform="rotate(-58)"/>
        <circle r="62" stroke="#8eaaa7" stroke-dasharray="50 339.6" transform="rotate(2)"/>
        <circle r="62" stroke="#333" stroke-dasharray="50 339.6" transform="rotate(62)"/>
        <circle r="62" stroke="#4a4a6c" stroke-dasharray="50 339.6" transform="rotate(122)"/>
        <circle r="62" stroke="#5d5f66" stroke-dasharray="50 339.6" transform="rotate(182)"/>
        <circle r="25" fill="#2a1580" stroke="none"/>
      </g>
      <g stroke="#333" stroke-width=".8" fill="none">
        <polyline points="103,30 112,30 132,55"/>
        <polyline points="103,117 114,117 128,117"/>
        <polyline points="103,191 110,191 135,165"/>
        <polyline points="274,22 262,22 245,50"/>
        <polyline points="274,180 262,180 252,160"/>
      </g>
    </svg>
    <div class="abs small" style="left:18px;top:25px;width:82px"><b style="font-size:7px;font-weight:600">Heading Here</b><br>Subtext here Subtext here Sub-text here Subtext here Subtext here Subtext here</div>
    <div class="abs small" style="left:18px;top:110px;width:82px"><b style="font-size:7px;font-weight:600">Heading Here</b><br>Subtext here Subtext here Sub-text here Subtext here Subtext here Subtext here</div>
    <div class="abs small" style="left:18px;top:185px;width:70px"><b style="font-size:7px;font-weight:600">Heading Here</b><br>Subtext here Subtext here Subtext here Sub-text here Subtext here Subtext here</div>
    <div class="abs small" style="right:22px;top:12px;width:86px;text-align:right"><b style="font-size:7px;font-weight:600">Heading Here</b><br>Subtext here Subtext here Sub-text here Subtext here Subtext here Subtext here</div>
    <div class="abs small" style="right:20px;top:90px;width:86px;text-align:right"><b style="font-size:7px;font-weight:600">Heading Here</b><br>Subtext here Subtext here Sub-text here Subtext here Subtext here Subtext here</div>
    <div class="abs small" style="right:22px;top:174px;width:86px"><b style="font-size:7px;font-weight:600;margin-left:33px">Heading Here</b><br>Subtext here Subtext here Sub-text here Subtext here Subtext here Subtext here</div>
  </div>
</section>

<section class="slide c1 r2">
  <header class="header"><h2>Project Title Here</h2><div class="brand">Brenwick &amp;<br>Associates</div></header>
  <ul class="body bullets" style="padding:16px 0 0 17px">
    <li>Subtext here Subtext here Subtext here Subtext here Subtext here</li>
    <li>Subtext here Subtext here Subtext here Subtext here Subtext here</li>
    <li>Subtext here Subtext here Subtext here Subtext here Subtext here</li>
    <li>Subtext here Subtext here Subtext here Subtext here Subtext here</li>
    <li>Subtext here Subtext here Subtext here Subtext here Subtext here</li>
    <li style="margin-top:3px">Subtext here Subtext here Subtext here Subtext here Subtext here</li>
    <li style="margin-top:6px">Subtext here Subtext here Subtext here Subtext here Subtext here</li>
  </ul>
</section>

<section class="slide c2 r2">
  <header class="header"><h2>Project Title Here</h2><div class="brand">Brenwick &amp;<br>Associates</div></header>
  <div class="body">
    <div class="abs" style="left:15px;top:20px;width:172px">
      <h3 class="h-violet" style="font-size:12.5px">Heading Here</h3>
      <p class="small" style="margin-top:2px">Subtext here Subtext here Subtext here Subtext here Subtext here Subtext here Subtext here Subtext here Subtext here Subtext here Subtext here Subtext here Subtext here Subtext here Subtext here Subtext here Subtext here Subtext here Subtext here Subtext here</p>
      <p class="small" style="margin-top:12px">Subtext here Subtext here Subtext here Subtext here Subtext here Subtext here Subtext here Subtext here Subtext here</p>
      <p class="small" style="margin-top:12px">Subtext here Subtext here Subtext here Subtext here Subtext here Subtext here Subtext here Subtext here Subtext here</p>
    </div>
    <div class="abs" style="left:202px;top:20px;width:172px">
      <h3 class="h-violet" style="font-size:12.5px">Heading Here</h3>
      <p class="small" style="margin-top:2px">Subtext here Subtext here Subtext here Subtext here Subtext here Subtext here Subtext here Subtext here Subtext here Subtext here Subtext here Subtext here Subtext here Subtext here Subtext here Subtext here Subtext here Subtext here Subtext here Subtext here</p>
      <p class="small" style="margin-top:12px">Subtext here Subtext here Subtext here Subtext here Subtext here Subtext here Subtext here Subtext here Subtext here</p>
      <p class="small" style="margin-top:12px">Subtext here Subtext here Subtext here Subtext here Subtext here Subtext here Subtext here Subtext here Subtext here</p>
    </div>
  </div>
</section>

<section class="slide c3 r2" style="background:#f6f7fb">
  <header class="header"><h2>Project Title Here</h2><div class="brand">Brenwick &amp;<br>Associates</div></header>
  <p class="abs small" style="left:18px;top:54px;width:350px">Lorem ipsum dolor sit Lorem ipsum dolor sit Lorem ipsum dolor sit Lorem ipsum dolor sit Lorem ipsum dolor sit Lorem ipsum dolor sit Lorem ipsum dolor sit Lorem ipsum dolor sit Lorem ipsum dolor sit Lorem ipsum dolor sit Lorem ipsum dolor sit Lorem ipsum dolor sit Lorem ipsum dolor sit Lorem ipsum dolor sit</p>
  <svg class="abs" style="left:0;top:0" width="386" height="130" aria-hidden="true"><line x1="70" y1="108" x2="318" y2="108" stroke="#1d8fc4" stroke-width="1.2"/></svg>
  <div class="year" style="left:57px;background:var(--navy-2)">1995</div>
  <div class="year" style="left:178px;background:var(--navy)">2005</div>
  <div class="year" style="left:301px;background:var(--slate)">2015</div>
  <div class="card" style="left:20px"><h4 style="background:var(--navy-2)">TITLE HERE</h4><p>Lorem ipsum dolor sit Lorem ipsum dolor sit Lorem ipsum dolor sit Lorem ipsum dolor sit Lorem ipsum dolor sit Lorem ipsum dolor sit Lorem ipsum dolor sit Lorem ipsum dolor sit</p></div>
  <div class="card" style="left:141px"><h4 style="background:var(--navy)">TITLE HERE</h4><p>Lorem ipsum dolor sit Lorem ipsum dolor sit Lorem ipsum dolor sit Lorem ipsum dolor sit Lorem ipsum dolor sit Lorem ipsum dolor sit Lorem ipsum dolor sit Lorem ipsum dolor sit</p></div>
  <div class="card" style="left:264px"><h4 style="background:var(--slate)">TITLE HERE</h4><p>Lorem ipsum dolor sit Lorem ipsum dolor sit Lorem ipsum dolor sit Lorem ipsum dolor sit Lorem ipsum dolor sit Lorem ipsum dolor sit Lorem ipsum dolor sit Lorem ipsum dolor sit</p></div>
</section>

<section class="slide c1 r3">
  <header class="header"><h2>Project Title Here</h2><div class="brand">Brenwick &amp;<br>Associates</div></header>
  <div class="body">
    <h3 class="abs h-violet" style="left:14px;top:13px;font-size:7.4px;color:var(--navy)">Bullet Title Heading Here Bullet Title Heading Here</h3>
    <p class="abs small" style="left:14px;top:24px;width:355px">Lorem ipsum dolor sit Lorem ipsum dolor sit Lorem ipsum dolor sit Lorem ipsum dolor sit Lorem ipsum dolor sit Lorem ipsum dolor sit Lorem ipsum dolor sit Lorem ipsum dolor sit Lorem ipsum dolor sit Lorem ipsum dolor sit Lorem ipsum dolor sit Lorem ipsum dolor sit Lorem ipsum</p>
    <svg class="abs" style="left:0;top:0" width="386" height="240" aria-label="Bar chart" role="img">
      <g font-family="Open Sans, Arial, sans-serif" font-size="5.6" fill="#555">
        <text x="20" y="77">Lorem ipsum dolor sit</text>
        <text x="20" y="92">Lorem ipsum dolor sit</text>
        <text x="20" y="110">Lorem ipsum dolor sit</text>
        <text x="20" y="128">Lorem ipsum dolor sit</text>
        <text x="20" y="145">Lorem ipsum dolor sit</text>
        <text x="20" y="164">Lorem ipsum dolor sit</text>
        <text x="20" y="207">Lorem ipsum dolor sit</text>
      </g>
      <line x1="93" y1="70" x2="93" y2="213" stroke="#bbb" stroke-width=".8"/>
      <g>
        <rect x="94" y="167" width="16" height="46" fill="#23106b"/>
        <rect x="113" y="132" width="20" height="81" fill="#261583"/>
        <rect x="137" y="146" width="19" height="67" fill="#231571"/>
        <rect x="160" y="173" width="19" height="40" fill="#3e12a8"/>
        <rect x="185" y="201" width="20" height="12" fill="#3b14b0"/>
        <rect x="209" y="209" width="24" height="4" fill="#777"/>
        <rect x="235" y="88" width="19" height="125" fill="#1f0f5e"/>
        <rect x="258" y="200" width="20" height="13" fill="#23106b"/>
        <rect x="282" y="207" width="20" height="6" fill="#3b14b0"/>
        <rect x="307" y="209" width="23" height="4" fill="#777"/>
      </g>
    </svg>
  </div>
</section>

<section class="slide c2 r3">
  <header class="header"><h2>Project Title Here</h2><div class="brand">Brenwick &amp;<br>Associates</div></header>
  <div class="body">
    <div class="abs" style="left:15px;top:21px;width:180px">
      <h3 class="h-violet" style="font-size:12.5px">Heading Here</h3>
      <p class="small" style="margin-top:4px;line-height:10.6px">Subtext here Subtext here Subtext here Subtext here Subtext here Subtext here Subtext here Subtext here Subtext here Subtext here Subtext here Subtext here Subtext here Subtext here Subtext here Subtext here Subtext here Subtext here Subtext here Subtext here</p>
      <p class="small" style="margin-top:10px;line-height:10.6px">Subtext here Subtext here Subtext here Subtext here Subtext here Subtext here Subtext here Subtext here Subtext here</p>
      <p class="small" style="margin-top:10px;line-height:10.6px">Subtext here Subtext here Subtext here Subtext here Subtext here Subtext here Subtext here Subtext here Subtext here</p>
    </div>
    <div class="ph" style="left:213px;top:30px;width:156px;height:85px"></div>
    <div class="ph" style="left:213px;top:131px;width:156px;height:85px"></div>
  </div>
</section>

<section class="slide c3 r3">
  <header class="header"><h2>Project Title Here</h2><div class="brand">Brenwick &amp;<br>Associates</div></header>
  <div class="body">
    <div class="abs" style="left:10px;top:17px;width:170px">
      <h3 class="h-violet" style="font-size:9.5px">Heading Here</h3>
      <p class="small" style="line-height:10.5px">Subtext here Subtext here Subtext here Subtext here Subtext here Subtext here Subtext here Subtext here</p>
    </div>
    <div class="abs" style="left:203px;top:17px;width:170px">
      <h3 class="h-violet" style="font-size:9.5px">Heading Here</h3>
      <p class="small" style="line-height:10.5px">Subtext here Subtext here Subtext here Subtext here Subtext here Subtext here Subtext here Subtext here</p>
    </div>
    <div class="ph" style="left:10px;top:51px;width:157px;height:84px"></div>
    <div class="ph" style="left:10px;top:144px;width:157px;height:84px"></div>
    <div class="ph" style="left:203px;top:51px;width:157px;height:84px"></div>
    <div class="ph" style="left:203px;top:144px;width:157px;height:84px"></div>
  </div>
</section>

<section class="slide c1 r4">
  <header class="header"><h2>Project Title Here</h2><div class="brand">Brenwick &amp;<br>Associates</div></header>
  <div class="body">
    <svg class="chev" style="top:36px" viewBox="0 0 48 46" aria-hidden="true"><polygon points="0,0 24,9 48,0 48,37 24,46 0,37" fill="#1f0f5e"/></svg>
    <div class="chev" style="top:36px"><span>Text Here</span></div>
    <div class="tbox" style="top:36px">› Lorem ipsum dolor sit ipsum Lorem ipsum dolor sit ipsum Lorem ipsum<br>› Lorem ipsum dolor sit ipsum Lorem ipsum dolor sit ipsum Lorem ipsum</div>

    <svg class="chev" style="top:79px" viewBox="0 0 48 46" aria-hidden="true"><polygon points="0,0 24,9 48,0 48,37 24,46 0,37" fill="#2e1370"/></svg>
    <div class="chev" style="top:79px"><span>Text Here</span></div>
    <div class="tbox" style="top:79px">› Lorem ipsum dolor sit ipsum Lorem ipsum dolor sit ipsum Lorem ipsum<br>› Lorem ipsum dolor sit ipsum Lorem ipsum dolor sit ipsum Lorem ipsum</div>

    <svg class="chev" style="top:121px" viewBox="0 0 48 46" aria-hidden="true"><polygon points="0,0 24,9 48,0 48,37 24,46 0,37" fill="#2a1a94"/></svg>
    <div class="chev" style="top:121px"><span>Text Here</span></div>
    <div class="tbox" style="top:121px">› Lorem ipsum dolor sit ipsum Lorem ipsum dolor sit ipsum Lorem ipsum<br>› Lorem ipsum dolor sit ipsum Lorem ipsum dolor sit ipsum Lorem ipsum</div>

    <svg class="chev" style="top:164px" viewBox="0 0 48 46" aria-hidden="true"><polygon points="0,0 24,9 48,0 48,37 24,46 0,37" fill="#1a1a7a"/></svg>
    <div class="chev" style="top:164px"><span>Text Here</span></div>
    <div class="tbox" style="top:164px">› Lorem ipsum dolor sit ipsum Lorem ipsum dolor sit ipsum Lorem ipsum<br>› Lorem ipsum dolor sit ipsum Lorem ipsum dolor sit ipsum Lorem ipsum</div>
  </div>
</section>

<section class="slide c2 r4">
  <header class="header"><h2>Project Title Here</h2><div class="brand">Brenwick &amp;<br>Associates</div></header>
  <div class="body">
    <h3 class="abs h-violet" style="left:28px;top:20px;font-size:7.4px;color:var(--navy)">Bullet Title Heading Here Bullet Title Heading Here</h3>
    <p class="abs small" style="left:28px;top:31px;width:340px">Lorem ipsum dolor sit Lorem ipsum dolor sit Lorem ipsum dolor sit Lorem ipsum dolor sit Lorem ipsum dolor sit Lorem ipsum dolor sit Lorem ipsum dolor sit Lorem ipsum dolor sit Lorem ipsum dolor sit Lorem ipsum dolor sit Lorem ipsum dolor sit Lorem ipsum dolor sit</p>
    <div class="abs" role="img" aria-label="Portrait photo of the company CEO" style="left:25px;top:93px;width:92px;height:92px;border-radius:50%;border:3px solid var(--navy);background:radial-gradient(circle at 50% 40%,#d8d8d8,#8a8a8a)"></div>
    <div class="abs" style="left:142px;top:75px;width:110px;height:68px;background:var(--cyan);padding:10px 9px;color:#fff">
      <p style="font-size:6.5px;font-weight:700">Company CEO Name</p>
      <p style="font-size:4.4px;line-height:8px;margin-top:3px">• ceo.name@social<br>• ceo.name@mailbox<br>• ceo.name@network<br>• ceo.name@profile</p>
    </div>
    <div class="abs" role="img" aria-label="Photo of a modern glass office building" style="left:142px;top:147px;width:110px;height:65px;background:linear-gradient(135deg,#cfe6f7,#4a90c8 55%,#1d5a97)"></div>
    <div class="abs" style="left:257px;top:75px;width:111px;height:137px;background:var(--navy);padding:8px 11px;color:#fff;font-size:5.6px;line-height:10.6px">Lorem ipsum dolor sit Lorem ipsum dolor sit Lorem ipsum dolor sit Lorem ipsum dolor sit Lorem ipsum dolor sit Lorem ipsum dolor sit Lorem ipsum dolor sit Lorem ipsum dolor sit Lorem ipsum dolor sit Lorem ipsum dolor sit Lorem ipsum dolor sit Lorem ipsum dolor sit</div>
  </div>
</section>

<section class="slide c3 r4" style="background:var(--navy)">
  <div class="abs" style="left:34px;top:124px;display:flex;align-items:center;gap:7px">
    <span style="width:14px;height:14px;border-radius:50%;background:#fff;display:block"></span>
    <span style="font-family:'Roboto Condensed',Arial,sans-serif;font-weight:700;font-size:15px;color:#fff;line-height:17px">Brenwick &amp;<br>Associates</span>
  </div>
  <h2 class="abs" style="left:205px;top:72px;font-family:'Roboto Condensed',Arial,sans-serif;font-weight:700;font-size:13.5px;color:#fff">THANKS FOR VALUBALE TIME</h2>
  <div class="thanks-box">
    <p>Lorem ipsum dolor sit amet,<br>consectetur adipiscing elit.<br>Donec accumsan.</p>
    <div style="margin-top:12px;font-size:9.4px;line-height:12px">
      <div style="display:flex;align-items:center;gap:6px"><svg width="8" height="8" viewBox="0 0 10 10" aria-hidden="true"><path d="M2 1l2 2-1 1.5c.7 1.3 1.2 1.8 2.5 2.5L7 6l2 2-1.5 1.5C4.5 9 1 5.5.5 2.5z" fill="#444"/></svg>: 555 0142 3386</div>
      <div style="display:flex;align-items:center;gap:6px"><svg width="8" height="8" viewBox="0 0 10 10" aria-hidden="true"><rect x="0.5" y="2" width="9" height="6" fill="#444"/><path d="M.5 2l4.5 3.5L9.5 2" stroke="#fff" fill="none" stroke-width=".8"/></svg>: abcde@brenwickmail.com</div>
      <div style="display:flex;align-items:center;gap:6px"><svg width="8" height="8" viewBox="0 0 10 10" aria-hidden="true"><path d="M9.5.5L.5 4.5l4 1 1 4z" fill="#444"/></svg>: brenwickassociates.com</div>
    </div>
  </div>
</section>

</body>
</html>
```